Personal Finance e-commerce website needs a simple budget design

Hello! I am starting to sell downloadable and printable budget planners, as shown in the attached file, for people to plan ahead on their personal finances. <br/><br/>I want to see a one-page design with similar columns (for example, "Expenses, Budget, and Actual"). I would also like to see the basic formula ("Net Income = Gross income - Total Expenses") somewhere on the design. Finally, I want the design to remain mostly minimalistic and simple for the average person to plan their personal monthly budgets.<br/><br/>However, other than that, the overall design, layout, and colors will be at the graphic designer's choice. If you have any questions for me, please let me know. Thank you for your time!

Industry/Entity Type

Financial Planning

Colors

Designer to choose colors to be used in the design.

Requirements
Must have
• I want to see a one-page design with similar columns (for example, "Expenses, Budget, and Actual").
• I want the design to remain mostly minimalistic and simple for the average person to plan their personal monthly budgets.
Nice to have
• I would also like to see the basic formula ("Net Income = Gross income - Total Expenses") somewhere on the design.

```html
<!DOCTYPE html>
<html lang="en">
<head>
<meta charset="utf-8">
<title>Basic Monthly Budget Planner</title>
<link href="https://fonts.googleapis.com/css2?family=Noto+Sans:wght@400;500&family=Open+Sans:wght@400&display=swap" rel="stylesheet">
<style>
  :root {
    --ink: #111111;
    --muted: #8a8a8a;
    --red: #b00a12;
    --red-soft: rgba(214, 140, 145, 0.82);
    --green: #7ccc1e;
    --green-bar: #76cf0c;
    --green-soft: rgba(196, 236, 170, 0.88);
    --blue: #3c3f7c;
    --blue-soft: rgba(160, 172, 200, 0.88);
    --paper: #f4f6f6;
    --band: rgba(255, 255, 255, 0.6);
  }
  * { margin: 0; padding: 0; box-sizing: border-box; }
  html, body { width: 929px; height: 1200px; overflow: hidden; background: var(--paper); }
  .sheet { position: relative; width: 929px; height: 1200px; overflow: hidden; font-family: "Noto Sans", sans-serif; color: var(--ink); }
  .backdrop {
    position: absolute; inset: 0;
    background:
      linear-gradient(225deg, #e6fbfc 0%, rgba(230, 251, 252, 0) 35%),
      linear-gradient(180deg, #f6f7f7 0%, #eceff0 45%, #dde6e8 100%);
  }
  .abs { position: absolute; }
  .brand { left: 166px; top: 58px; width: 184px; height: 138px; }
  .brand-text { left: 166px; top: 80px; width: 184px; text-align: center; }
  .brand-logo { font-size: 35px; line-height: 44px; }
  .brand-name { font-size: 20px; line-height: 28px; }
  .title { left: 480px; top: 58px; width: 394px; text-align: right; font-size: 36px; font-weight: 500; white-space: nowrap; }
  .title .accent { color: var(--red); }
  .field-line { height: 3px; background: var(--ink); border-radius: 50%; top: 158px; }
  .field-label { top: 164px; font-size: 17px; text-align: center; }
  .header-band { left: 0; top: 204px; width: 929px; height: 58px; background: var(--band); }
  .col-head { top: 208px; font-size: 36px; font-weight: 500; white-space: nowrap; }
  .col-head.expenses { left: 50px; color: var(--red); }
  .col-head.budget { left: 424px; color: var(--green); }
  .col-head.actual { left: 671px; color: var(--blue); }
  .col-note { font-family: "Open Sans", sans-serif; font-size: 18px; line-height: 24px; color: var(--muted); text-align: center; }
  .rows { top: 323px; display: flex; flex-direction: column; gap: 9.3px; }
  .rows div { height: 57px; }
  .rows.expenses { left: 45px; width: 352px; }
  .rows.expenses div { background: var(--red-soft); }
  .rows.budget { left: 424px; width: 226px; }
  .rows.budget div { background: var(--green-soft); }
  .rows.actual { left: 671px; width: 214px; }
  .rows.actual div { background: var(--blue-soft); }
  .formula-bar { left: 45px; top: 1001px; width: 840px; height: 56px; background: var(--green-bar); }
  .formula-bar .total { position: absolute; left: 576px; top: 0; width: 264px; height: 56px; background: var(--red); }
  .term { top: 1008px; font-size: 32px; color: #fff; text-align: center; white-space: nowrap; }
  .operator { width: 56px; height: 56px; border-radius: 50%; background: #fff; top: 1001px; display: flex; align-items: center; justify-content: center; font-size: 34px; font-weight: 500; }
  .operator.eq { left: 278px; color: var(--green-bar); border: 2px solid var(--green-bar); }
  .operator.minus { left: 592px; color: var(--red); border: 2px solid var(--red); }
  .explain-band { left: 45px; top: 1065px; width: 840px; height: 58px; background: var(--band); }
  .explain { font-size: 19px; line-height: 23px; color: var(--muted); text-align: center; letter-spacing: 0.3px; }
  .stem { width: 3px; height: 68px; top: 1060px; background: #444; border-radius: 2px; }
  .site { left: 0; width: 929px; top: 1144px; text-align: center; font-size: 18px; }
</style>
</head>
<body>
<main class="sheet">
  <div class="backdrop" role="img" aria-label="Soft pale cyan and grey abstract background"></div>

  <svg class="abs brand" viewBox="0 0 184 138" aria-hidden="true">
    <ellipse cx="92" cy="69" rx="91" ry="68" fill="none" stroke="#111" stroke-width="1.3"/>
  </svg>
  <div class="abs brand-text">
    <div class="brand-logo">Logo</div>
    <div class="brand-name">Company name</div>
  </div>

  <h1 class="abs title">Basic Monthly <span class="accent">Budget</span></h1>
  <div class="abs field-line" style="left:526px;width:162px"></div>
  <div class="abs field-label" style="left:526px;width:162px">Month</div>
  <div class="abs field-line" style="left:705px;width:164px"></div>
  <div class="abs field-label" style="left:705px;width:164px">Year</div>

  <div class="abs header-band"></div>
  <h2 class="abs col-head expenses">Expenses (category)</h2>
  <h2 class="abs col-head budget">Budget (USD)</h2>
  <h2 class="abs col-head actual">Actual (USD)</h2>
  <p class="abs col-note" style="left:98px;width:200px;top:266px">Custom category</p>
  <p class="abs col-note" style="left:444px;width:190px;top:270px">What you plan to<br>spend</p>
  <p class="abs col-note" style="left:681px;width:200px;top:268px">What you actually<br>spent</p>

  <div class="abs rows expenses"><div></div><div></div><div></div><div></div><div></div><div></div><div></div><div></div><div></div><div></div></div>
  <div class="abs rows budget"><div></div><div></div><div></div><div></div><div></div><div></div><div></div><div></div><div></div><div></div></div>
  <div class="abs rows actual"><div></div><div></div><div></div><div></div><div></div><div></div><div></div><div></div><div></div><div></div></div>

  <div class="abs formula-bar"><div class="total"></div></div>
  <div class="abs explain-band"></div>
  <div class="abs stem" style="left:305px"></div>
  <div class="abs stem" style="left:619px"></div>
  <div class="abs term" style="left:75px;width:200px">Net Income</div>
  <div class="abs term" style="left:357px;width:220px">Gross Income</div>
  <div class="abs term" style="left:650px;width:232px">Total Expenses</div>
  <div class="abs operator eq">=</div>
  <div class="abs operator minus">−</div>

  <p class="abs explain" style="left:65px;width:220px;top:1070px">How much money<br>you kept</p>
  <p class="abs explain" style="left:357px;width:220px;top:1070px">How much money<br>you earned</p>
  <p class="abs explain" style="left:654px;width:220px;top:1082px">Actual Expenses</p>

  <p class="abs site">www.Web page.com</p>
</main>
</body>
</html>
```